One of a Kind Clean Business Card

We need to design a new business card template for our company. Our company designs and produced merchandising displays. You can see a sample of what we produce on our site www.qorvatfixtures.com. I have uploaded our logo in vector format, as well as a picture of our current business cards. We want a totally different look. We want simple and clean, looking forward to seeing what people create.
Updates

I would like to update the address for Tellur Display Group Inc. 418 N Brindle Ave Corvane Heights, IL 60817 Would also note. No QR codes

Industry/Entity Type

Business

Contact Information for Business Card

Need a 1 sided business card designed.

Font styles to use
Serif

Requirements
Must have
• Easy to view; Clean Design
Nice to have
• Features that promote engineering and creativity
Should not have
• Too much clutter, keep it simple

```html
<!DOCTYPE html>
<html lang="en">
<head>
<meta charset="utf-8">
<title>Tellur Display Group Inc. – Business Card</title>
<link rel="stylesheet" href="https://fonts.googleapis.com/css2?family=Libre+Baskerville:wght@400;700&family=Playfair+Display:wght@700&display=swap">
<style>
  :root {
    --stage: #2b2a2a;
    --card-black: #0d0b0b;
    --card-red: #a3212a;
    --bar-red: #7d0f17;
    --bar-edge: #c23a43;
    --ink-dark: #1c0507;
    --ink-light: #f4eeee;
    --ink-soft: #f1c9cc;
  }
  * { box-sizing: border-box; margin: 0; padding: 0; }
  html, body {
    width: 1200px; height: 799px; overflow: hidden;
    background: var(--stage);
  }
  .stage {
    width: 1200px; height: 799px;
    display: flex; align-items: center; justify-content: center;
  }
  .card {
    width: 420px; height: 735px;
    display: flex; flex-direction: column;
    box-shadow: 0 18px 40px rgba(0,0,0,.45);
    font-family: "Libre Baskerville", serif;
  }
  .card__brand {
    flex: 0 0 455px;
    background: var(--card-black);
    display: flex; align-items: center;
    padding: 0 48px;
  }
  .brand-name {
    color: var(--ink-light);
    font-size: 26px;
    line-height: 1.35;
    letter-spacing: 1.5px;
    text-transform: uppercase;
  }
  .card__contact {
    flex: 1;
    background: var(--card-red);
    padding: 18px 24px 22px;
    display: flex; flex-direction: column;
  }
  .person-name {
    align-self: flex-end;
    font-family: "Playfair Display", serif;
    font-weight: 700;
    font-size: 26px;
    letter-spacing: 2px;
    color: var(--ink-dark);
    text-transform: uppercase;
  }
  .company-line {
    align-self: flex-end;
    font-size: 13px;
    color: var(--ink-dark);
    margin: 4px 0 14px;
  }
  .contact-list {
    list-style: none;
    display: flex; flex-direction: column; gap: 9px;
    flex: 1;
  }
  .contact-row {
    flex: 1;
    background: var(--bar-red);
    border: 1px solid var(--bar-edge);
    display: flex; align-items: center;
    padding: 0 12px;
    gap: 12px;
    color: var(--ink-soft);
    font-size: 12px;
    white-space: nowrap;
  }
  .contact-icon { width: 16px; height: 16px; flex: 0 0 16px; }
  .contact-icon path { fill: var(--ink-dark); }
</style>
</head>
<body>
  <main class="stage">
    <article class="card">
      <header class="card__brand">
        <span class="brand-name">Tellur Display Group Inc.</span>
      </header>
      <section class="card__contact">
        <h1 class="person-name">Nolan Vestri</h1>
        <p class="company-line">Tellur Display Group Inc.</p>
        <ul class="contact-list">
          <li class="contact-row">
            <svg class="contact-icon" viewBox="0 0 20 20" aria-hidden="true">
              <path d="M10 1a6.5 6.5 0 0 0-6.5 6.5C3.5 12.5 10 19 10 19s6.5-6.5 6.5-11.5A6.5 6.5 0 0 0 10 1zm0 9a2.5 2.5 0 1 1 0-5 2.5 2.5 0 0 1 0 5z"/>
            </svg>
            <span>418 N Brindle Ave, Corvane Heights, IL 60817</span>
          </li>
          <li class="contact-row">
            <svg class="contact-icon" viewBox="0 0 20 20" aria-hidden="true">
              <path d="M5 1.5 8 5.5 6.3 7.6c1.1 2.4 3.5 4.8 6.1 6.1L14.5 12l4 3-1.8 3.2C9.5 18.6 1.4 10.5 1.8 3.3z"/>
            </svg>
            <span>Phone: 555.014.0193</span>
          </li>
          <li class="contact-row">
            <svg class="contact-icon" viewBox="0 0 20 20" aria-hidden="true">
              <path d="M10 1a9 9 0 1 0 0 18 9 9 0 0 0 0-18zm5.9 8h-2.9a13 13 0 0 0-1.3-5.6A7 7 0 0 1 15.9 9zM10 3.2c.9 1.3 1.5 3.4 1.6 5.8H8.4c.1-2.4.7-4.5 1.6-5.8zM8.3 3.4A13 13 0 0 0 7 9H4.1a7 7 0 0 1 4.2-5.6zM4.1 11H7a13 13 0 0 0 1.3 5.6A7 7 0 0 1 4.1 11zm5.9 5.8c-.9-1.3-1.5-3.4-1.6-5.8h3.2c-.1 2.4-.7 4.5-1.6 5.8zm1.7-.2A13 13 0 0 0 13 11h2.9a7 7 0 0 1-4.2 5.6z"/>
            </svg>
            <span>www.qorvatfixtures.com</span>
          </li>
        </ul>
      </section>
    </article>
  </main>
</body>
</html>
```